Chinese Herbal and Roots Shop design

Hello Designers,

We are a herbal startup company which sells Chinese Herbal Products. we are looking for a responsive and unqiue Ecommerce web design.
Our business name is velorin and our area of business cut across the entire United States.

We don't have a logo at the moment and designers who come up with a great logo is more likely to be awarded winner of the consent.

The design needs to be completely custom design and we are not after just a template design. Please be creative and at the same time design have to be professionally looking and easy to navigate.
A theme which suits a herbal products are desired. We are open to different colors excpet RED and PINK.

NAVIGATION
Header -
Home, products, offers, Blog, cart, login/account

Footer -
Please refer to other Ecommerce websites

Page requires:
HOME PAGE
1. slider(Highlist products)
2. FEATURE PRODUCTS
3. Latest products
4. Most selling products
5. Deal of the day
6. Email capture (Newsletter/signup)
7. Social media links
8. Footer

PRODUCT PAGE
All the products will be present here with required details (price, short note and offers if any)

PRODUCT DETAILS PAGE
A well designed detailed page for a particular product covers the details of the price, increment, short description, purchase and other add to cart button. A section with similar products should be listed below aswell.

Industry/Entity Type

It Company

Coding

Coded - Design and coding required

```html
<!DOCTYPE html>
<html lang="en">
<head>
<meta charset="utf-8">
<title>velorin – Chinese Herbal Products</title>
<link rel="stylesheet" href="https://fonts.googleapis.com/css2?family=Courgette&family=Montserrat:wght@400;600;700&family=Roboto:wght@300;400;500;700;900&family=Open+Sans:wght@400;600&family=Playfair+Display:wght@700&family=PT+Sans:wght@700&display=swap">
<style>
:root{
  --green:#6aaa2a;
  --green-dark:#2f7a35;
  --green-deep:#1f5a2a;
  --lime:#8cc63f;
  --olive:#9aa51f;
  --brown:#3b2418;
  --ink:#222;
  --muted:#777;
  --card:#f1efeb;
  --star:#f39a2b;
  --star-off:#d4d4d4;
  --band:#e8e8e8;
}
*{box-sizing:border-box;margin:0;padding:0}
html,body{width:1200px;height:2703px;overflow:hidden;background:#fff}
body{position:relative;font-family:'Roboto',sans-serif;color:var(--ink)}
.abs{position:absolute}

/* header */
.brand{position:absolute;display:flex;align-items:center;gap:12px;font-family:'Roboto',sans-serif;font-weight:500;color:var(--green-dark)}
.brand-dot{width:20px;height:20px;border-radius:50%;background:var(--green)}
.header .brand{left:88px;top:38px;font-size:58px;line-height:1}
.account{left:876px;top:22px;font-family:'Montserrat',sans-serif;font-size:12px;display:flex;align-items:center;gap:8px}
.cart{left:1038px;top:20px;display:flex;align-items:center}
.cart-count{width:22px;height:22px;border-radius:50%;background:var(--lime);font-size:11px;display:flex;align-items:center;justify-content:center;margin-left:-4px;font-family:'Montserrat',sans-serif}
.nav{left:640px;top:64px;display:flex;font-family:'Montserrat',sans-serif;font-size:12px;font-weight:600;letter-spacing:.2px}
.nav a{color:var(--ink);text-decoration:none;padding:9px 12px;margin-right:18px}
.nav a.active{background:var(--green);color:#fff}
.header-rule{left:0;top:122px;width:1200px;height:8px;background:var(--green-dark)}

/* hero */
.hero{left:0;top:130px;width:1200px;height:410px;overflow:hidden}
.hero-copy{left:500px;top:78px;width:640px;text-align:center}
.hero-title{font-family:'Courgette',cursive;font-size:43px;color:#111;font-weight:400}
.hero-sub{font-family:'Open Sans',sans-serif;font-size:32px;color:var(--olive);margin-top:12px}
.btn-shop{left:708px;top:360px;width:198px;height:53px;background:var(--green-deep);color:#fff;font-family:'Roboto',sans-serif;font-weight:900;font-size:25px;display:flex;align-items:center;justify-content:center;gap:8px;border-radius:2px}

/* section titles */
.section-title{left:0;width:1200px;text-align:center;font-family:'Courgette',cursive;font-size:46px;color:var(--brown);font-weight:400}

/* product cards */
.card{position:absolute;width:177px;text-align:center}
.card-media{position:relative;width:177px;height:209px;background:var(--card);display:flex;align-items:center;justify-content:center}
.bottle{width:88px;height:150px;border-radius:14px 14px 8px 8px;background:linear-gradient(180deg,#dcdcdc 0 14%,#fff 14% 30%,#2f8a4f 30% 80%,#f4f4f4 80%)}
.bottle.amber{background:linear-gradient(180deg,#c9a35a 0 14%,#3a2a1a 14% 100%)}
.bottle.white{background:linear-gradient(180deg,#eef2f0 0 14%,#fbfbfb 14% 35%,#2d8a7a 35% 75%,#fbfbfb 75%)}
.bottle.dark{background:linear-gradient(180deg,#c9a35a 0 14%,#163f22 14% 100%)}
.add-cart{position:absolute;left:30px;top:100px;width:124px;height:38px;background:#fff;font-family:'Roboto',sans-serif;font-size:13px;display:flex;align-items:center;justify-content:center;gap:4px}
.sale{position:absolute;right:0;top:0}
.card-name{font-family:'Montserrat',sans-serif;font-size:10px;font-weight:600;margin:18px -12px 0;white-space:nowrap;letter-spacing:0}
.stars{font-size:11px;letter-spacing:1px;margin-top:5px;color:var(--star-off)}
.stars b{color:var(--star);font-weight:400}
.price{font-family:'Open Sans',sans-serif;font-size:21px;margin-top:4px}
.price s{color:#888;margin-right:10px}

/* most selling */
.selling{left:11px;top:1106px;width:612px;height:330px;background:linear-gradient(90deg,#f7f8f6,#eceeea 60%,#f3f4f1)}
.selling h2{position:absolute;left:73px;top:47px;font-family:'Roboto',sans-serif;font-size:29px;font-weight:900;color:var(--ink)}
.selling h2 span{color:var(--green);font-weight:400}
.selling .lead{position:absolute;left:73px;top:91px;font-size:13.5px;color:#888}
.selling .rule{position:absolute;left:73px;top:120px;width:24px;height:3px;background:var(--green)}
.selling .body{position:absolute;left:73px;top:132px;width:520px;font-size:11px;line-height:22px;color:#777}
.btn-buy{position:absolute;left:75px;top:200px;width:168px;height:47px;background:var(--green-deep);color:#fff;font-weight:700;font-size:19px;display:flex;align-items:center;justify-content:center;gap:10px;border-radius:2px}
.ceo{left:625px;top:1106px;width:575px;height:330px;background:linear-gradient(135deg,#6bb034,#5c9f28)}
.ceo .quote{position:absolute;left:33px;top:40px;width:54px;height:50px;background:var(--green-deep);border-radius:50% 50% 50% 0;color:#fff;font-size:34px;font-weight:900;display:flex;align-items:center;justify-content:center;font-family:'Roboto',sans-serif}
.ceo h3{position:absolute;left:141px;top:36px;color:#fff;font-size:27px;font-weight:900}
.ceo h3 span{font-weight:400}
.ceo .rule{position:absolute;left:141px;top:76px;width:28px;height:3px;background:#fff}
.ceo p{position:absolute;left:141px;top:96px;width:405px;color:#fff;font-size:11px;line-height:22px}
.ceo .avatar{position:absolute;left:141px;top:179px;width:47px;height:48px;background:linear-gradient(180deg,#d8d8d8,#8a8a8a)}
.ceo .who{position:absolute;left:201px;top:186px;color:#fff}
.ceo .who strong{display:block;font-size:14px;margin-bottom:4px}
.ceo .who span{font-size:11px}
.signature{position:absolute;left:141px;top:248px;width:170px;height:40px;background:linear-gradient(90deg,rgba(255,255,255,.35),rgba(255,255,255,.15))}

.btn-more{left:505px;top:2009px;width:181px;height:33px;border-radius:17px;background:var(--green-dark);color:#fff;font-family:'Montserrat',sans-serif;font-size:12px;font-weight:700;display:flex;align-items:center;justify-content:center;gap:10px}

/* newsletter */
.newsletter{left:0;top:2103px;width:1200px;height:256px;background:radial-gradient(circle at 30% 40%,#336f3f,#2a6236 60%,#265a31)}
.newsletter h2{position:absolute;left:0;top:60px;width:1200px;text-align:center;color:#fff;font-family:'PT Sans',sans-serif;font-size:40px}
.subscribe{position:absolute;left:463px;top:137px;width:308px;height:45px;background:#fff;border-radius:23px;display:flex;overflow:hidden}
.subscribe .field{flex:1;padding-left:26px;display:flex;align-items:center;color:#666;font-family:Georgia,serif;font-size:15px}
.subscribe .submit{width:137px;background:var(--lime);border-radius:23px;color:#1f4a22;font-family:'Montserrat',sans-serif;font-weight:700;font-size:13px;display:flex;align-items:center;justify-content:center;gap:8px}

/* footer */
.footer .brand{left:94px;top:2430px;font-size:54px;line-height:1}
.footer-about{left:94px;top:2528px;width:300px;font-size:12.5px;line-height:19px;color:#555}
.footer-col{position:absolute;top:2410px}
.footer-col h4{font-family:'Playfair Display',serif;font-size:16px;color:#333;margin-bottom:22px;letter-spacing:.3px}
.footer-col ul{list-style:none}
.footer-col li{font-size:13px;color:#555;height:33.5px}
.footer-col li.hl{color:var(--green)}
.contact li{display:flex;gap:14px;align-items:center}
.contact li svg{flex:none}
.socials{left:836px;top:2607px;display:flex;gap:14px}
.socials span{width:33px;height:33px;border-radius:50%;border:1px solid #e4e4e4;display:block}
.copyright{left:0;top:2659px;width:1200px;height:44px;background:var(--band);display:flex;align-items:center;justify-content:center;font-size:12.5px;color:#555}
</style>
</head>
<body>

<header class="header">
  <div class="brand"><span class="brand-dot"></span>velorin</div>
  <div class="abs account">
    <svg width="16" height="16" viewBox="0 0 16 16"><path d="M8 2a6 6 0 1 1-5.6 8" fill="none" stroke="#333" stroke-width="1.5"/><path d="M1 8h8M6 5l3 3-3 3" fill="none" stroke="#333" stroke-width="1.5"/></svg>
    Login / Account
  </div>
  <div class="abs cart">
    <svg width="22" height="20" viewBox="0 0 22 20"><path d="M1 2h4l3 11h10l3-8H7" fill="none" stroke="#222" stroke-width="2"/><circle cx="9" cy="17" r="2" fill="#222"/><circle cx="17" cy="17" r="2" fill="#222"/></svg>
    <span class="cart-count">0</span>
  </div>
  <nav class="abs nav">
    <a class="active" href="#">HOME</a><a href="#">PRODUCTS</a><a href="#">OFFERS</a><a href="#">BLOG</a><a href="#">CONTACT US</a>
  </nav>
  <div class="abs header-rule"></div>
</header>

<section class="abs hero">
  <svg class="abs" style="left:0;top:0" width="1200" height="410" viewBox="0 0 1200 410">
    <defs>
      <linearGradient id="heroBg" x1="0" x2="1" y1="0" y2="0">
        <stop offset="0" stop-color="#cfe3a6"/><stop offset=".5" stop-color="#e7f0d2"/><stop offset="1" stop-color="#b8d77a"/>
      </linearGradient>
      <linearGradient id="heroWave" x1="0" x2="1"><stop offset="0" stop-color="#4f9a22"/><stop offset="1" stop-color="#7cba2f"/></linearGradient>
    </defs>
    <rect width="1200" height="410" fill="url(#heroBg)"/>
    <path d="M0 230 C300 300 700 330 1200 150 L1200 300 C800 420 300 330 0 300Z" fill="url(#heroWave)"/>
    <path d="M0 270 C300 340 800 380 1200 260 L1200 410 L0 410Z" fill="#fff"/>
  </svg>
  <div class="abs" role="img" aria-label="Three herbal supplement bottles" style="left:63px;top:77px;width:442px;height:315px;background:linear-gradient(90deg,#1f5a2a,#2f7a35 40%,#d9a12a 55%,#1f5a2a 75%,#e8e4d8);border-radius:18px;opacity:.9"></div>
  <div class="abs hero-copy">
    <h1 class="hero-title">Chinese Herbal Products</h1>
    <p class="hero-sub">Natural Diet Support</p>
  </div>
</section>
<div class="abs btn-shop">SHOP NOW <svg width="10" height="14" viewBox="0 0 10 14"><path d="M1 1l8 6-8 6z" fill="#fff"/></svg></div>

<h2 class="abs section-title" style="top:590px">Feature Products</h2>

<div class="card" style="left:90px;top:704px">
  <div class="card-media"><div class="bottle" role="img" aria-label="Supplement bottle"></div><div class="add-cart">ADD TO CART <span>→</span></div></div>
  <div class="card-name">FUSCE ALIQUAM VARIABLE – V2</div>
  <div class="stars"><b>★★★</b>★★</div>
  <div class="price"><s>$18.55</s>$17.00</div>
</div>
<div class="card" style="left:299px;top:704px">
  <div class="card-media"><div class="bottle amber" role="img" aria-label="Supplement jar"></div></div>
  <div class="card-name">FUSCE ALIQUAM VARIABLE – V2</div>
  <div class="stars"><b>★★</b>★★★</div>
  <div class="price">$22</div>
</div>
<div class="card" style="left:515px;top:704px">
  <div class="card-media"><div class="bottle white" role="img" aria-label="Tea blend bottle"></div>
    <svg class="sale" width="38" height="46" viewBox="0 0 38 46"><path d="M0 0h38v46l-19-12L0 46z" fill="#8cc63f"/><text x="19" y="18" font-size="9" fill="#fff" text-anchor="middle" font-family="Montserrat,sans-serif" font-weight="700">SALE!</text></svg>
  </div>
  <div class="card-name">FUSCE ALIQUAM VARIABLE – V2</div>
  <div class="stars"><b>★★★★</b>★</div>
  <div class="price"><s>$19.20</s>$15.20</div>
</div>
<div class="card" style="left:726px;top:704px">
  <div class="card-media"><div class="bottle dark" role="img" aria-label="Supplement bottle"></div></div>
  <div class="card-name">FUSCE ALIQUAM VARIABLE – V1</div>
  <div class="stars"><b>★</b>★★★★</div>
  <div class="price">$18.55</div>
</div>
<div class="card" style="left:937px;top:704px">
  <div class="card-media"><div class="bottle" role="img" aria-label="Supplement bottle"></div></div>
  <div class="card-name">FUSCE ALIQUAM VARIABLE – V2</div>
  <div class="stars"><b>★★★★</b>★</div>
  <div class="price">$20</div>
</div>

<section class="abs selling" role="img" aria-label="Faded photo of smiling people">
  <h2>MOST <span>SELLING PRODUCTS</span></h2>
  <p class="lead">Lorem Ipsum Dolor Some Link Sit Amet, Cum At Inani Interesset</p>
  <div class="rule"></div>
  <p class="body">We're extremely proud of what we've achieved together with charitie lorem individuals, philanthropists and schools since the Green Hand was founded in 2007, and here are some fact from our achivemnet.</p>
  <div class="btn-buy">Buy Now <svg width="8" height="12" viewBox="0 0 8 12"><path d="M1 1l6 5-6 5z" fill="#fff"/></svg></div>
</section>

<section class="abs ceo">
  <div class="quote">“</div>
  <h3>WORD FROM <span>CEO</span></h3>
  <div class="rule"></div>
  <p>How to pursue pleasure rationally consequences that are extremeely painful or again is there anyones who loves or pursues or desires to obtain pain of itself because its sed great pleasure get well soon.</p>
  <div class="avatar" role="img" aria-label="Portrait of the CEO"></div>
  <div class="who"><strong>Marcus Hale</strong><span>CEO of Leafwell</span></div>
  <div class="signature" role="img" aria-label="Handwritten signature"></div>
</section>

<h2 class="abs section-title" style="top:1530px">Latest Products</h2>

<div class="card" style="left:90px;top:1654px">
  <div class="card-media"><div class="bottle" role="img" aria-label="Supplement bottle"></div><div class="add-cart">ADD TO CART <span>→</span></div></div>
  <div class="card-name">FUSCE ALIQUAM VARIABLE – V2</div>
  <div class="stars"><b>★★★</b>★★</div>
  <div class="price"><s>$18.55</s>$17.00</div>
</div>
<div class="card" style="left:299px;top:1654px">
  <div class="card-media"><div class="bottle amber" role="img" aria-label="Supplement jar"></div></div>
  <div class="card-name">FUSCE ALIQUAM VARIABLE – V2</div>
  <div class="stars"><b>★★</b>★★★</div>
  <div class="price">$22</div>
</div>
<div class="card" style="left:515px;top:1654px">
  <div class="card-media"><div class="bottle white" role="img" aria-label="Tea blend bottle"></div>
    <svg class="sale" width="38" height="46" viewBox="0 0 38 46"><path d="M0 0h38v46l-19-12L0 46z" fill="#8cc63f"/><text x="19" y="18" font-size="9" fill="#fff" text-anchor="middle" font-family="Montserrat,sans-serif" font-weight="700">SALE!</text></svg>
  </div>
  <div class="card-name">FUSCE ALIQUAM VARIABLE – V2</div>
  <div class="stars"><b>★★★★</b>★</div>
  <div class="price"><s>$19.20</s>$15.20</div>
</div>
<div class="card" style="left:726px;top:1654px">
  <div class="card-media"><div class="bottle dark" role="img" aria-label="Supplement bottle"></div></div>
  <div class="card-name">FUSCE ALIQUAM VARIABLE – V1</div>
  <div class="stars"><b>★</b>★★★★</div>
  <div class="price">$18.55</div>
</div>
<div class="card" style="left:937px;top:1654px">
  <div class="card-media"><div class="bottle" role="img" aria-label="Supplement bottle"></div></div>
  <div class="card-name">FUSCE ALIQUAM VARIABLE – V2</div>
  <div class="stars"><b>★★★★</b>★</div>
  <div class="price">$20</div>
</div>

<div class="abs btn-more">
  <svg width="14" height="14" viewBox="0 0 14 14"><path d="M2 7a5 5 0 1 0 2-4" fill="none" stroke="#fff" stroke-width="2"/><path d="M1 1v4h4" fill="none" stroke="#fff" stroke-width="2"/></svg>
  LOAD MORE
</div>

<section class="abs newsletter">
  <h2>Stay in Touch with Updates</h2>
  <div class="subscribe">
    <div class="field">Enter you email</div>
    <div class="submit"><svg width="14" height="10" viewBox="0 0 14 10"><rect width="14" height="10" rx="1" fill="#1f4a22"/><path d="M0 0l7 5 7-5" fill="none" stroke="#8cc63f" stroke-width="1.2"/></svg>SUBMIT</div>
  </div>
</section>

<footer class="footer">
  <div class="brand"><span class="brand-dot"></span>velorin</div>
  <p class="abs footer-about">Sed eleifend, lacus nec bibendum pulvinar, nibh mauris vehicula augue, sit amet mattis ligula lorem eu nisl. Integer a egestas mauris.</p>
  <div class="footer-col" style="left:416px">
    <h4>Infomation</h4>
    <ul><li>New Products</li><li>Top Sellers</li><li>Our Blog</li><li>About Our Shop</li><li class="hl">– &nbsp;Secure Shopping</li></ul>
  </div>
  <div class="footer-col" style="left:609px">
    <h4>My Account</h4>
    <ul><li>My Account</li><li>Personal Infomation</li><li>Addresses</li><li>Discount</li><li>Orders History</li></ul>
  </div>
  <div class="footer-col contact" style="left:838px">
    <h4>Contact</h4>
    <ul>
      <li><svg width="12" height="12" viewBox="0 0 12 12"><path d="M1 6l5-5 5 5v5H1z" fill="#888"/></svg>18 Linden Avenue, Portland, USA</li>
      <li><svg width="12" height="12" viewBox="0 0 12 12"><path d="M2 1h3l1 3-2 1a7 7 0 0 0 3 3l1-2 3 1v3c-6 1-10-3-9-9z" fill="#888"/></svg>0014 555 0137</li>
      <li><svg width="12" height="10" viewBox="0 0 12 10"><rect width="12" height="10" rx="1" fill="#888"/><path d="M0 0l6 5 6-5" fill="none" stroke="#fff"/></svg>hello@leafmart.com</li>
      <li class="hl"><svg width="12" height="12" viewBox="0 0 12 12"><circle cx="6" cy="6" r="5" fill="none" stroke="#888" stroke-width="1.4"/><path d="M1 6h10M6 1c3 3 3 7 0 10M6 1c-3 3-3 7 0 10" fill="none" stroke="#888"/></svg>www.leafmartstore.com</li>
    </ul>
  </div>
  <div class="abs socials"><span></span><span></span><span></span><span></span></div>
  <div class="abs copyright">velorin © 2016 All Rights Reserved Terms of Use and Privacy Policy</div>
</footer>

</body>
</html>
```